business card for a shoe shop

we would like a business card for a family owned shoe shop.
With this information included.
Darnell's Shoe Store
Family owned since 1947

then on other side
Darnell's Shoe Store
Footwear fitting specialist
Phone: 9187 2630
218 Quarry St, Fernleigh Downs 3187
(cnr. Hartwick Rd and Quarry St)
darnellshoes218@examplemail.com
if could incorporate the purple color on card i have attached.

```html
<!DOCTYPE html>
<html lang="en">
<head>
<meta charset="utf-8">
<title>Darnell's Shoe Store – Business Card</title>
<link rel="stylesheet" href="https://fonts.googleapis.com/css2?family=Sacramento&family=Arimo:wght@400&display=swap">
<style>
  :root {
    --backdrop: #dddddd;
    --brand-purple: #8557f1;
    --purple-echo: #7a4be3;
    --lavender-echo: #f0ecfd;
    --ink: #111111;
    --paper: #ffffff;
  }
  * { margin: 0; padding: 0; box-sizing: border-box; }
  html, body {
    width: 1200px; height: 1000px; overflow: hidden;
    background: var(--backdrop);
    font-family: "Arimo", Arial, sans-serif;
  }
  .card {
    position: absolute;
    left: 277px; width: 647px; height: 388px;
    overflow: hidden;
    text-align: center;
  }
  .card--front { top: 80px; background: var(--brand-purple); color: var(--paper); }
  .card--back { top: 532px; background: var(--paper); color: var(--ink); }

  .name-echo {
    position: absolute;
    left: 8px; top: -40px;
    font-family: "Sacramento", cursive;
    font-size: 360px; line-height: 1;
    white-space: nowrap;
    transform: rotate(-4deg);
    transform-origin: left top;
    pointer-events: none;
  }
  .card--front .name-echo { color: var(--purple-echo); }
  .card--back .name-echo { color: var(--lavender-echo); }

  .shop-name {
    position: absolute; left: 0; right: 0;
    font-family: "Sacramento", cursive;
    font-size: 68px; line-height: 1;
    font-weight: 400;
    white-space: nowrap;
  }
  .card--front .shop-name { top: 120px; }
  .card--back .shop-name { top: 45px; }

  .tagline {
    position: absolute; left: 0; right: 0;
    font-size: 18.5px; letter-spacing: 3px;
    text-transform: uppercase;
    font-weight: 400;
  }
  .card--front .tagline { top: 218px; }
  .card--back .tagline { top: 145px; }

  .heart-mark {
    position: absolute; left: 50%;
    width: 32px; height: 28px;
    transform: translateX(-50%);
  }
  .card--front .heart-mark { top: 268px; }

  .divider {
    position: absolute; top: 188px; left: 127px; width: 393px; height: 24px;
  }
  .divider .rule {
    position: absolute; top: 11px; height: 2px; width: 174px; background: var(--ink);
  }
  .divider .rule--left { left: 0; }
  .divider .rule--right { right: 0; }
  .divider .heart-mark { top: 0; width: 26px; height: 23px; }

  .contact-line {
    position: absolute; left: 0; right: 0;
    display: flex; justify-content: center; align-items: flex-start;
    gap: 8px;
    font-size: 17px; line-height: 20px;
  }
  .contact-line svg { flex: none; fill: var(--brand-purple); }
  .contact--phone { top: 234px; }
  .contact--address { top: 273px; }
  .contact--email { top: 331px; gap: 12px; }
  .address-lines { text-align: center; }
</style>
</head>
<body>

<section class="card card--front" aria-label="Business card front">
  <span class="name-echo" aria-hidden="true">Darnell</span>
  <h1 class="shop-name">Darnell's Shoe Store</h1>
  <p class="tagline">Family owned since 1947</p>
  <svg class="heart-mark" viewBox="0 0 32 28" aria-hidden="true">
    <path fill="#ffffff" d="M16 28 C6 20 0 14 0 8 C0 3.5 3.5 0 8 0 C11.5 0 14.5 2 16 5 C17.5 2 20.5 0 24 0 C28.5 0 32 3.5 32 8 C32 14 26 20 16 28 Z"/>
  </svg>
</section>

<section class="card card--back" aria-label="Business card back">
  <span class="name-echo" aria-hidden="true">Darnell</span>
  <h2 class="shop-name">Darnell's Shoe Store</h2>
  <p class="tagline">Footwear fitting specialist</p>
  <div class="divider" aria-hidden="true">
    <span class="rule rule--left"></span>
    <svg class="heart-mark" viewBox="0 0 32 28">
      <path fill="#111111" d="M16 28 C6 20 0 14 0 8 C0 3.5 3.5 0 8 0 C11.5 0 14.5 2 16 5 C17.5 2 20.5 0 24 0 C28.5 0 32 3.5 32 8 C32 14 26 20 16 28 Z"/>
    </svg>
    <span class="rule rule--right"></span>
  </div>

  <p class="contact-line contact--phone">
    <svg width="18" height="18" viewBox="0 0 24 24" aria-hidden="true">
      <path d="M6.6 10.8c1.4 2.8 3.8 5.1 6.6 6.6l2.2-2.2c.3-.3.7-.4 1-.2 1.1.4 2.3.6 3.6.6.6 0 1 .4 1 1V20c0 .6-.4 1-1 1C10.6 21 3 13.4 3 4c0-.6.4-1 1-1h3.5c.6 0 1 .4 1 1 0 1.3.2 2.5.6 3.6.1.3 0 .7-.2 1l-2.3 2.2z"/>
    </svg>
    <span>9187 2630</span>
  </p>

  <div class="contact-line contact--address">
    <svg width="16" height="20" viewBox="0 0 16 20" aria-hidden="true">
      <path d="M8 0C3.6 0 0 3.5 0 7.8 0 13.5 8 20 8 20s8-6.5 8-12.2C16 3.5 12.4 0 8 0zm0 11a3.2 3.2 0 1 1 0-6.4A3.2 3.2 0 0 1 8 11z"/>
    </svg>
    <p class="address-lines">218 Quarry St, Fernleigh Downs 3187<br>(cnr. Hartwick Rd and Quarry St)</p>
  </div>

  <p class="contact-line contact--email">
    <svg width="20" height="15" viewBox="0 0 20 15" style="margin-top:3px" aria-hidden="true">
      <path d="M0 0h20v1.2L10 8 0 1.2z"/>
      <path d="M0 3.2l10 6.8 10-6.8V15H0z"/>
    </svg>
    <span>darnellshoes218@examplemail.com</span>
  </p>
</section>

</body>
</html>
```